Business Card Design

Hello!
We would like you to design some business cards for us. We will send you a sample of what we have. We want to take out the Tidewell Harbor Logo and add the RZD logo. This is the company that we own and it manages 7 to 8 franchised child care locations called Pebble Grove. So you can make the Pebble Grove a little logo smaller than what it currently is. Currently the back of the card lists the locations but we don't need that as we are adding new locations every few months. We can also add the website address for RZD below the logo if needed. We don't like the current design so please change it up as you like. Please let us know if you have any questions.

Industry/Entity Type

Business

Contact Information for Business Card

See above

Font styles to use
Serif
Sans Serif

Colors

Designer to choose colors to be used in the design.

Requirements
Must have
• Clean crisp look

```html
<!DOCTYPE html>
<html lang="en">
<head>
<meta charset="utf-8">
<title>Pebble Grove – Business Card</title>
<link rel="stylesheet" href="https://fonts.googleapis.com/css2?family=Libre+Baskerville:wght@400;700&family=Montserrat:wght@400;500;600&display=swap">
<style>
  :root {
    --brand-red: #a8333a;
    --brand-red-dark: #8e2a30;
    --ink: #2b2b2b;
    --muted: #6f6f6f;
    --rule: #8a8a8a;
    --paper: #ffffff;
    --backdrop: #ece9e5;
    --serif: "Libre Baskerville", Georgia, serif;
    --sans: "Montserrat", Arial, sans-serif;
  }
  * { box-sizing: border-box; margin: 0; padding: 0; }
  html, body { width: 1200px; height: 1000px; overflow: hidden; }
  body { background: var(--backdrop); position: relative; font-family: var(--sans); }

  .card {
    position: absolute;
    width: 520px;
    height: 296px;
    box-shadow: 0 6px 18px rgba(0,0,0,0.18);
  }

  /* Front side */
  .card--front { left: 110px; top: 170px; background: var(--paper); }
  .name-block {
    position: absolute; left: 298px; top: 0; width: 196px; height: 118px;
    background: var(--brand-red); color: var(--paper);
    padding: 38px 0 0 22px;
  }
  .name-block__name { font-family: var(--serif); font-weight: 700; font-size: 27px; line-height: 1; }
  .name-block__title { font-family: var(--sans); font-size: 13px; letter-spacing: 0.5px; margin-top: 8px; }

  .brand {
    position: absolute; left: 30px; top: 146px;
    display: flex; align-items: center; gap: 10px;
  }
  .brand__dot { width: 16px; height: 16px; border-radius: 50%; background: var(--brand-red); }
  .brand__name { font-family: var(--serif); font-weight: 400; font-size: 26px; color: var(--brand-red); }

  .rule { position: absolute; height: 1px; background: var(--rule); }
  .rule--top { left: 240px; right: 28px; top: 136px; }
  .rule--bottom { left: 30px; right: 250px; top: 232px; }

  .contact {
    position: absolute; left: 300px; top: 158px;
    list-style: none; font-size: 12.5px; color: var(--muted);
  }
  .contact li { display: flex; align-items: center; gap: 8px; height: 20px; }
  .contact svg { width: 12px; height: 12px; fill: var(--brand-red); flex: none; }

  .office { position: absolute; left: 30px; top: 242px; }
  .office__label { font-size: 14px; font-weight: 500; color: var(--brand-red); }
  .office__address { font-size: 12.5px; color: var(--muted); line-height: 1.3; margin-top: 2px; }

  /* Back side */
  .card--back {
    left: 570px; top: 530px; background: var(--brand-red);
    display: flex; flex-direction: column; align-items: center; justify-content: center; gap: 18px;
  }
  .emblem {
    width: 132px; height: 132px; border-radius: 50%; background: var(--paper);
    box-shadow: 0 6px 0 var(--brand-red-dark);
  }
  .card--back .brand__name { color: var(--paper); font-size: 24px; }
</style>
</head>
<body>

<section class="card card--front" aria-label="Business card front">
  <div class="name-block">
    <p class="name-block__name">Dev Marlowe</p>
    <p class="name-block__title">ACADEMY OWNER</p>
  </div>

  <div class="rule rule--top"></div>

  <div class="brand">
    <span class="brand__dot"></span>
    <span class="brand__name">Pebble Grove</span>
  </div>

  <ul class="contact">
    <li>
      <svg viewBox="0 0 24 24" aria-hidden="true"><path d="M6.6 10.8a15.1 15.1 0 0 0 6.6 6.6l2.2-2.2a1 1 0 0 1 1-.25 11.4 11.4 0 0 0 3.6.57 1 1 0 0 1 1 1V20a1 1 0 0 1-1 1A17 17 0 0 1 3 4a1 1 0 0 1 1-1h3.5a1 1 0 0 1 1 1c0 1.25.2 2.45.57 3.57a1 1 0 0 1-.25 1z"/></svg>
      555 - 210 - 4477
    </li>
    <li>
      <svg viewBox="0 0 24 24" aria-hidden="true"><path d="M2 5h20v14H2z M2 5l10 8 10-8" /><path d="M2 5h20L12 12z" fill="#fff" opacity=".5"/></svg>
      dev.marlowe@pebblegrove.net
    </li>
    <li>
      <svg viewBox="0 0 24 24" aria-hidden="true"><path d="M12 2a10 10 0 1 0 0 20 10 10 0 0 0 0-20zm0 2c.9 1.1 1.6 2.5 2 4h-4c.4-1.5 1.1-2.9 2-4zM4.3 14a8 8 0 0 1 0-4h3.4a16 16 0 0 0 0 4zm.9 2h3a13 13 0 0 0 1.4 3.6A8 8 0 0 1 5.2 16zm3-8h-3a8 8 0 0 1 4.4-3.6A13 13 0 0 0 8.2 8zM12 20c-.9-1.1-1.6-2.5-2-4h4c-.4 1.5-1.1 2.9-2 4zm2.3-6H9.7a14 14 0 0 1 0-4h4.6a14 14 0 0 1 0 4zm.1 5.6A13 13 0 0 0 15.8 16h3a8 8 0 0 1-4.4 3.6zM16.3 14a16 16 0 0 0 0-4h3.4a8 8 0 0 1 0 4zm-.5-6a13 13 0 0 0-1.4-3.6A8 8 0 0 1 18.8 8z"/></svg>
      www.pebblegrove.net
    </li>
  </ul>

  <div class="rule rule--bottom"></div>

  <div class="office">
    <p class="office__label">Management Offices</p>
    <p class="office__address">1840 Orchard Lane, Suite G<br>Maple Ridge, IL 60412</p>
  </div>
</section>

<section class="card card--back" aria-label="Business card back">
  <span class="emblem"></span>
  <span class="brand__name">Pebble Grove</span>
</section>

</body>
</html>
```